Landing Page für Freelancer im Bereich der Informationstechnik
Zielgruppe
Ich bin Experte für Informationstechnik, Unified Communications, Beratung, Management sowie Projekte aller Art.
Mit meiner WOLKENTOR GmbH bin ich als (einzelner) Freelancer für mittelständische Unternehmen und Konzerne in verschiedensten Projekten tätig.
Mein Motto lautet 'Mit Präzision und langjähriger Erfahrung immer alles im Griff!'
Aufgabenstellung
Die aktuell existierende Internet-Präsenz unter wolkentor-web.de beinhaltet aktuell nur eine minimalistische statische Seite sowie das Impressum, ohne jegliche dynamische Inhalte.
DABEI SOLL ES BLEIBEN. Auch die Inhalte sollen unverändert übernommen werden.
Lediglich soll jetzt eine Anlehnung an das zwischenzeitlich vorhandene Logo vorgenommen werden, welches ich mitliefere.
Es geht mir insgesamt nur darum, ein professionelleres Auftreten zu haben, WENN sich denn mal jemand auf die Seite verirrt.
Das Aussehen soll daher modern und dynamisch sein.
ZUSAMMENFASSUNG: Inhalte bleiben 1:1, grafische Anpassung an Logo gewünscht.
Technisch: Statisch, kein Content-Management. Lohnt sich hier nicht.
SEHR WICHTIG: Ich möchte gerne, dass die Lieferung bereits als HTML (und NICHT NUR ALS GRAFIK) erfolgt, ggf. stelle ich auch kurz den FTP-Zugang.
Insgesamt möchte ich gar keine große Sache draus machen.
Viele Anpassungsrunden wird es voraussichtlich nicht geben.
Zeitlich ist dies hier ein sehr kleines Projekt - Erweiterungen kommen später.

```html
<!DOCTYPE html>
<html lang="de">
<head>
<meta charset="utf-8">
<title>WOLKENTOR GmbH – Malte Johannes Brenner</title>
<link rel="stylesheet" href="https://fonts.googleapis.com/css2?family=Montserrat:wght@500;600;700&display=swap">
<style>
  :root {
    --teal: #4ba3bf;
    --teal-line: #8ccbd9;
    --ink: #484848;
    --white: #ffffff;
    --panel: rgba(228, 238, 242, 0.9);
  }
  * { box-sizing: border-box; margin: 0; padding: 0; }
  html, body { width: 1097px; height: 1200px; overflow: hidden; background: var(--white); }
  body { font-family: "Montserrat", Arial, sans-serif; color: var(--ink); position: relative; }

  .hero {
    position: absolute; left: 0; top: 0; width: 1097px; height: 507px;
    background:
      radial-gradient(ellipse 330px 200px at 780px 250px, rgba(240, 120, 120, 0.85), rgba(240,120,120,0) 70%),
      radial-gradient(ellipse 260px 160px at 840px 360px, rgba(140, 210, 235, 0.8), rgba(140,210,235,0) 70%),
      linear-gradient(100deg, #1f6f86 0%, #4aa6c2 35%, #2f7e98 60%, #6fb9d2 85%, #c9dbe3 100%);
  }
  .hero-panel {
    position: absolute; left: 106px; top: 39px; width: 433px; height: 433px;
    background: var(--panel);
    display: flex; flex-direction: column; align-items: center;
  }
  .brand {
    margin-top: 150px; display: flex; align-items: center; gap: 10px;
    font-size: 22px; font-weight: 600; letter-spacing: 3px; color: var(--teal);
  }
  .brand-mark { width: 12px; height: 12px; background: var(--teal); }
  .motto {
    margin-top: 108px; text-align: center; text-transform: uppercase;
    font-size: 17px; font-weight: 600; line-height: 29px; color: var(--ink);
  }

  .degree { position: absolute; left: 106px; top: 602px; font-size: 21px; font-weight: 600; }
  .name { position: absolute; left: 104px; top: 650px; font-size: 40px; font-weight: 600; color: var(--teal); letter-spacing: -0.5px; }
  .master { position: absolute; left: 106px; top: 718px; font-size: 21px; font-weight: 600; }

  .email {
    position: absolute; left: 106px; top: 828px; font-size: 12px; font-weight: 600;
    color: var(--ink); text-decoration: none; border-bottom: 1px solid var(--teal-line); padding-bottom: 3px;
  }
  .expertise {
    position: absolute; left: 446px; top: 822px; width: 560px;
    font-size: 29px; font-weight: 600; line-height: 41px; letter-spacing: -0.3px;
  }
  .intro {
    position: absolute; left: 446px; top: 972px; width: 560px;
    font-size: 12px; font-weight: 600; line-height: 19px;
  }

  .divider { position: absolute; left: 106px; top: 1092px; width: 885px; height: 1px; background: var(--teal-line); }
  .footer-nav { position: absolute; left: 106px; top: 1140px; display: flex; gap: 38px; }
  .footer-nav a { font-size: 12.5px; font-weight: 600; color: var(--ink); text-decoration: none; }
</style>
</head>
<body>
  <header class="hero" role="img" aria-label="Futuristischer Raum mit leuchtenden Neonrahmen und großer Bildwand in Rot und Blau">
    <div class="hero-panel">
      <div class="brand"><span class="brand-mark"></span>WOLKENTOR GmbH</div>
      <p class="motto">"Mit Präzision und<br>langjähriger Erfahrung immer<br>alles im Griff!"</p>
    </div>
  </header>

  <p class="degree">Diplom-Informatiker (FH)</p>
  <h1 class="name">Malte Johannes Brenner</h1>
  <p class="master">Master of Science in Electronic Business</p>

  <a class="email" href="#">m punkt brenner at wolkentor-web punkt de</a>

  <h2 class="expertise">Experte für Informationstechnik | Unified Communications | Beratung | Management | Projekte aller Art</h2>
  <p class="intro">Gerne schicke ich Ihnen unverbindlich mein Expertenprofil samt CV sowie meine aktuellen Verfügbarkeiten zu. Kontaktieren Sie mich hierzu einfach per E-Mail unter m punkt brenner at wolkentor-web punkt de. Ich freue mich auf Sie!</p>

  <div class="divider"></div>
  <nav class="footer-nav">
    <a href="#">Startseite</a>
    <a href="#">Impressum</a>
    <a href="#">Datenschutz</a>
  </nav>
</body>
</html>
```